Pelton|Marsh & Quillan business card contest

We need a logo for an upscale boutique diversified company involved in real estate, investments, cattle, and more. Our businesses DO NOT need to be reflected in the business card nor do we want them noted. This is our logo and colors and we love our logo and colors. Our logo looks best against a black background and we like to include the firm name in our logo usage. importantly, the names Pelton and Marsh are separated by | not / and we use an ampersand not the word and.
On the front of the card, we want to include:
company logo and name (Pelton|Marsh & Quillan)
on the back, we would definitely include:
address, email, cell #
logo and name (smaller size than front)

The variable will be location of individual name and title (mine for example is ) - whether on the front OR on the back. interested in variations from which to choose
Dr. Neil R. Whitcombe, CFA
Scientifique des Fusées Financières

we would like to use contemporary symbols for address, email address, cell # with an option for web site that we do not intend to use initially. we like two sided cards and believe this design should use four rounded corners with the standard size. we prefer thicker card stock and may look at metal.

```html
<!DOCTYPE html>
<html lang="en">
<head>
<meta charset="UTF-8">
<title>Pelton|Marsh &amp; Quillan — Business Card</title>
<link href="https://fonts.googleapis.com/css2?family=Oswald:wght@300;400;500;600&display=swap" rel="stylesheet">
<style>
  :root {
    --stage: #dedede;
    --card-dark: #1c1c1c;
    --card-light: #fbfbfb;
    --brand-orange: #d8731f;
    --ink-grey: #5a5a5a;
    --ink-soft: #6e6e6e;
    --ink-black: #151515;
    --mark-light: #e4e4e4;
  }
  * { margin: 0; padding: 0; box-sizing: border-box; }
  html, body {
    width: 1200px;
    height: 757px;
    overflow: hidden;
  }
  body {
    background: var(--stage);
    font-family: "Oswald", "Arial Narrow", sans-serif;
    position: relative;
  }
  .card {
    position: absolute;
    top: 293px;
    width: 484px;
    height: 288px;
    border-radius: 18px;
    overflow: hidden;
  }
  .card--front {
    left: 79px;
    background: var(--card-dark);
    display: flex;
    align-items: center;
    justify-content: center;
  }
  .card--back {
    left: 621px;
    background: var(--card-light);
  }
  .wordmark {
    font-weight: 400;
    letter-spacing: 0.5px;
    white-space: nowrap;
  }
  .wordmark--front {
    color: var(--mark-light);
    font-size: 38px;
    margin-top: 4px;
  }
  .brand-block {
    position: absolute;
    left: 20px;
    width: 204px;
    top: 100px;
    display: flex;
    flex-direction: column;
    align-items: center;
  }
  .brand-square {
    width: 22px;
    height: 22px;
    background: var(--brand-orange);
    margin-bottom: 12px;
  }
  .wordmark--back {
    color: var(--ink-grey);
    font-size: 19px;
  }
  .divider {
    position: absolute;
    left: 242px;
    top: 62px;
    width: 2px;
    height: 180px;
    background: var(--brand-orange);
  }
  .details {
    position: absolute;
    left: 265px;
    top: 84px;
  }
  .person-name {
    color: var(--brand-orange);
    font-size: 18px;
    font-weight: 400;
    line-height: 1.2;
  }
  .person-name .credential {
    color: var(--ink-soft);
    font-size: 11px;
    margin-left: 4px;
    letter-spacing: 0.3px;
  }
  .person-title {
    color: var(--ink-soft);
    font-size: 14px;
    font-weight: 300;
    margin-top: 1px;
  }
  .contact-list {
    list-style: none;
    margin-top: 21px;
  }
  .contact-item {
    display: flex;
    align-items: center;
    gap: 10px;
    color: var(--ink-grey);
    font-size: 12.5px;
    font-weight: 300;
    height: 20px;
  }
  .contact-icon {
    width: 12px;
    height: 12px;
    fill: var(--ink-black);
    flex-shrink: 0;
  }
  .address {
    margin-top: 9px;
    font-style: normal;
    color: var(--ink-black);
    font-size: 12.5px;
    font-weight: 500;
    line-height: 1.42;
    letter-spacing: 0.2px;
  }
</style>
</head>
<body>

  <section class="card card--front" aria-label="Card front">
    <div class="wordmark wordmark--front">Pelton|Marsh &amp; Quillan</div>
  </section>

  <section class="card card--back" aria-label="Card back">
    <div class="brand-block">
      <div class="brand-square"></div>
      <div class="wordmark wordmark--back">Pelton|Marsh &amp; Quillan</div>
    </div>

    <div class="divider"></div>

    <div class="details">
      <h1 class="person-name">Dr. Neil R. Whitcombe<span class="credential">CFA</span></h1>
      <p class="person-title">Scientifique des Fusées Financières</p>

      <ul class="contact-list">
        <li class="contact-item">
          <svg class="contact-icon" viewBox="0 0 12 12" aria-hidden="true">
            <path d="M1 4.2c0-1.3 2.2-2.4 5-2.4s5 1.1 5 2.4v.8H8.6v-1c-.8-.3-1.6-.4-2.6-.4s-1.8.1-2.6.4v1H1z"/>
            <path d="M3 5.6h6l1.4 4.6H1.6z"/>
          </svg>
          <span>+1 913 555 0147</span>
        </li>
        <li class="contact-item">
          <svg class="contact-icon" viewBox="0 0 12 12" aria-hidden="true">
            <path d="M1 2.5h10v7H1z"/>
            <path d="M1.6 3.1 6 6.6l4.4-3.5" fill="none" stroke="#fbfbfb" stroke-width="1"/>
          </svg>
          <span>hello@peltonmarsh.com</span>
        </li>
      </ul>

      <address class="address">
        2275 Larkspur Avenue,<br>
        Suite 310, Kansas 66209
      </address>
    </div>
  </section>

</body>
</html>
```